MORVEK IT Limited Buisness card logo

I am setting up a IT Consultancy company and want a logo that is related to the IT industry, but also i am thinking that the A in MOR and the A in VEK are linked together maybe horizontally and vertically, also thought about the A being @ as it symbolises IT services. This logo will be used on paperwork, business cards and website.

Industry/Entity Type

Business

Contact Information for Business Card

Gareth Wilmslow
MORVEK IT Limited
IT Consultant
Mobile: 07912563084
Email: garethwk@fernmail.co.uk

Requirements
Must have
• IT Theme

```html
<!DOCTYPE html>
<html lang="en">
<head>
<meta charset="utf-8">
<title>MORVEK IT Limited — Business Card</title>
<link href="https://fonts.googleapis.com/css2?family=Questrial&display=swap" rel="stylesheet">
<style>
  :root {
    --page-bg: #f2f2f2;
    --card-white: #ffffff;
    --card-fade: #ececec;
    --ink-black: #111214;
    --panel-dark: #16181b;
    --panel-darker: #0b0c0e;
    --accent-blue: #3c66b4;
    --accent-blue-light: #4f7fd0;
    --text-light: #f4f4f4;
    --divider: #8a8d92;
    --mark-square: #1a1c20;
  }
  * { margin: 0; padding: 0; box-sizing: border-box; }
  html, body {
    width: 1200px;
    height: 900px;
    overflow: hidden;
    background: var(--page-bg);
    font-family: "Questrial", "Century Gothic", sans-serif;
  }
  .canvas {
    position: relative;
    width: 1200px;
    height: 900px;
  }
  .business-card {
    position: absolute;
    left: 150px;
    top: 193px;
    width: 900px;
    height: 514px;
    border-radius: 40px;
    overflow: hidden;
    background: linear-gradient(180deg, var(--card-fade) 0%, var(--card-white) 45%);
    box-shadow: 0 14px 40px rgba(0, 0, 0, 0.18);
  }
  .brand-block {
    position: absolute;
    left: 0;
    top: 0;
    width: 100%;
    height: 300px;
    display: flex;
    flex-direction: column;
    align-items: center;
  }
  .brand-square {
    margin-top: 34px;
    width: 150px;
    height: 150px;
    border-radius: 18px;
    background: var(--mark-square);
  }
  .brand-name {
    margin-top: 34px;
    font-size: 54px;
    letter-spacing: 4px;
    color: var(--ink-black);
    text-transform: uppercase;
    line-height: 1;
  }
  .accent-stripe {
    position: absolute;
    left: 0;
    top: 300px;
    width: 100%;
    height: 14px;
    background: linear-gradient(90deg, var(--accent-blue) 0%, var(--accent-blue-light) 100%);
  }
  .contact-panel {
    position: absolute;
    left: 0;
    top: 314px;
    width: 100%;
    height: 200px;
    background: linear-gradient(180deg, var(--panel-dark) 0%, var(--panel-darker) 100%);
    display: flex;
    align-items: center;
    justify-content: center;
  }
  .person {
    text-align: right;
    padding-right: 28px;
  }
  .person-name {
    font-size: 38px;
    color: var(--accent-blue-light);
    line-height: 1.15;
  }
  .person-role {
    font-size: 34px;
    color: var(--text-light);
    line-height: 1.25;
  }
  .panel-divider {
    width: 2px;
    height: 100px;
    background: var(--divider);
  }
  .contact-list {
    list-style: none;
    padding-left: 24px;
  }
  .contact-item {
    display: flex;
    align-items: center;
    gap: 10px;
    font-size: 32px;
    color: var(--text-light);
    line-height: 1.3;
    letter-spacing: 1px;
  }
  .contact-icon {
    width: 28px;
    height: 28px;
    flex: none;
  }
</style>
</head>
<body>
<main class="canvas">
  <article class="business-card">
    <header class="brand-block">
      <div class="brand-square"></div>
      <h1 class="brand-name">MORVEK IT Limited</h1>
    </header>
    <div class="accent-stripe"></div>
    <section class="contact-panel">
      <div class="person">
        <p class="person-name">Gareth Wilmslow</p>
        <p class="person-role">IT Consultant</p>
      </div>
      <div class="panel-divider"></div>
      <ul class="contact-list">
        <li class="contact-item">
          <svg class="contact-icon" viewBox="0 0 24 24" aria-hidden="true">
            <path fill="#4f7fd0" d="M6.6 10.8a15.1 15.1 0 0 0 6.6 6.6l2.2-2.2a1 1 0 0 1 1-.25 11.4 11.4 0 0 0 3.6.57 1 1 0 0 1 1 1V20a1 1 0 0 1-1 1A17 17 0 0 1 3 4a1 1 0 0 1 1-1h3.5a1 1 0 0 1 1 1c0 1.25.2 2.45.57 3.57a1 1 0 0 1-.25 1z"/>
          </svg>
          <span>07912563084</span>
        </li>
        <li class="contact-item">
          <svg class="contact-icon" viewBox="0 0 24 24" aria-hidden="true">
            <rect x="2" y="5" width="20" height="14" rx="1.5" fill="#4f7fd0"/>
            <path d="M2.5 6l9.5 7 9.5-7" fill="none" stroke="#16181b" stroke-width="1.6"/>
          </svg>
          <span>garethwk@fernmail.co.uk</span>
        </li>
      </ul>
    </section>
  </article>
</main>
</body>
</html>
```